Peaks4U LOGO + Business Card design for a Ski Tour agency

- New start-up international tour agency focused on skiing tours
- Connected with the Alps
- Targeted at Asians
- Business/Brand name: Peaks4U

```html
<!DOCTYPE html>
<html lang="en">
<head>
<meta charset="UTF-8">
<title>Peaks4U Business Card</title>
<link href="https://fonts.googleapis.com/css2?family=Open+Sans:wght@400;600;700&display=swap" rel="stylesheet">
<style>
  :root {
    --brand-red: #c01f2f;
    --brand-red-dark: #a01826;
    --ink-grey: #58595b;
    --ink-dark: #3a3a3c;
    --paper: #ffffff;
    --backdrop: #2b2b2d;
  }
  * { box-sizing: border-box; margin: 0; padding: 0; }
  html, body {
    width: 1200px; height: 880px; overflow: hidden;
    background: var(--backdrop);
    font-family: "Open Sans", Arial, sans-serif;
  }
  .stage {
    position: relative; width: 1200px; height: 880px;
  }
  .card {
    position: absolute; left: 300px;
    width: 600px; height: 343px;
    border-radius: 22px;
    box-shadow: 0 10px 28px rgba(0,0,0,0.45);
    overflow: hidden;
  }
  /* Front */
  .card-front { top: 70px; background: var(--brand-red); color: var(--paper); }
  .front-brand {
    position: absolute; left: 0; right: 0; top: 92px;
    display: flex; align-items: center; justify-content: center; gap: 16px;
  }
  .brand-dot {
    width: 56px; height: 56px; border-radius: 50%;
    background: var(--paper);
  }
  .front-brand .brand-name {
    font-size: 62px; font-weight: 600; letter-spacing: 1px; color: var(--paper);
  }
  .front-web {
    position: absolute; left: 0; right: 0; top: 210px;
    text-align: center; font-size: 15px; letter-spacing: 4px; color: var(--paper);
  }
  /* Back */
  .card-back { top: 463px; background: var(--paper); }
  .back-brand {
    position: absolute; left: 48px; top: 60px;
    font-size: 50px; font-weight: 600; color: var(--ink-grey); letter-spacing: 1px;
  }
  .person { position: absolute; left: 50px; top: 140px; }
  .person-name { font-size: 21px; font-weight: 700; color: var(--ink-grey); line-height: 1.1; }
  .person-role { font-size: 15px; color: var(--brand-red); line-height: 1.2; }
  .address {
    position: absolute; left: 50px; top: 198px;
    font-size: 14px; color: var(--ink-dark); line-height: 1.35;
  }
  .contacts {
    position: absolute; left: 50px; top: 244px; list-style: none;
    font-size: 14px; color: var(--ink-dark);
  }
  .contacts li { display: flex; align-items: center; gap: 8px; height: 22px; }
  .contacts .accent { color: var(--brand-red); }
  .contact-icon { width: 16px; height: 16px; flex: none; }
  .back-mark {
    position: absolute; right: 60px; top: 56px;
    width: 220px; height: 220px; border-radius: 50%;
    background: var(--brand-red);
  }
</style>
</head>
<body>
<main class="stage">
  <section class="card card-front" aria-label="Card front">
    <div class="front-brand">
      <span class="brand-dot"></span>
      <span class="brand-name">Peaks4U</span>
    </div>
    <p class="front-web">www.PEAKS4UWEB.com</p>
  </section>

  <section class="card card-back" aria-label="Card back">
    <h1 class="back-brand">Peaks4U</h1>
    <div class="person">
      <p class="person-name">Liam Carter</p>
      <p class="person-role">Owner</p>
    </div>
    <p class="address">PO BOX 456, Ridge Road<br>3rd Lane, Alpine 67890</p>
    <ul class="contacts">
      <li>
        <svg class="contact-icon" viewBox="0 0 16 16" aria-hidden="true">
          <circle cx="8" cy="8" r="7.3" fill="none" stroke="var(--brand-red)" stroke-width="1.4"/>
          <rect x="5.5" y="3.8" width="5" height="8.4" rx="1" fill="none" stroke="var(--brand-red)" stroke-width="1.2"/>
        </svg>
        <span>555.010.2040</span>
      </li>
      <li>
        <svg class="contact-icon" viewBox="0 0 16 16" aria-hidden="true">
          <circle cx="8" cy="8" r="8" fill="var(--brand-red)"/>
          <rect x="4" y="5.2" width="8" height="5.6" fill="var(--paper)"/>
          <path d="M4 5.2 L8 8.5 L12 5.2" fill="none" stroke="var(--brand-red)" stroke-width="1"/>
        </svg>
        <span>hello@peaks4umail.com</span>
      </li>
      <li>
        <svg class="contact-icon" viewBox="0 0 16 16" aria-hidden="true">
          <circle cx="8" cy="8" r="8" fill="var(--brand-red)"/>
          <circle cx="8" cy="8" r="4.5" fill="none" stroke="var(--paper)" stroke-width="1"/>
          <path d="M3.5 8 H12.5 M8 3.5 V12.5" stroke="var(--paper)" stroke-width="1"/>
        </svg>
        <span>www.<span class="accent">peaks4uweb</span>.com</span>
      </li>
    </ul>
    <div class="back-mark" aria-hidden="true"></div>
  </section>
</main>
</body>
</html>
```